Elegant and modern Wedding Photography brochure

My existing brochure (attached) needs a major facelift. This is one of the main selling tools - it gets emailed to my clients when they make an equiry on what packages i offer and it is printed out and walked through at our first meeting. This brochure is as critical as my website - it needs to sing!

I'm looking for an eye-catching design that says:
Elegant
Modern
Clean
Crisp
Not cutesy or lovey-dovey thanks - we are more sophisticated and professional than that.

Update images to some of the latest weddings I've shot also. Let me know files and resolution you need. I've enabled right-click to download images on my site for a limited time. Please note that I retain copyright and will pursue any breeches.

Http://www.clarapennock.com/Melbourne-wedding-photography
Updates

Thanks for all of your designs! Will take a few days to decide.

Target Market(s)

Australian Women aged 24-44

Industry/Entity Type

Wedding

Font styles to use
Other font styles liked:
• Century Gothic

Requirements
Must have
• Easy to print - does not have to be 6 A4 pages like the existing brochure
Nice to have
• Some full page images - The photos are supposed to be the hero here :-)
Should not have
• Not cutesy or lovey-dovey thanks - we are more sophisticated and professional than that.

No black backgrounds, I prefer a white thanks

No images in organic shaped boxes (like the rectangles in the logo - no thanks).
Keep the lines straight and sharp

```html
<!DOCTYPE html>
<html lang="en">
<head>
<meta charset="utf-8">
<title>Clara Pennock – Wedding Photography Brochure</title>
<link href="https://fonts.googleapis.com/css2?family=Questrial&family=Great+Vibes&display=swap" rel="stylesheet">
<style>
:root{
  --paper:#ffffff;
  --stage:#ffffff;
  --ink:#3c3c3c;
  --soft-ink:#7a7a7a;
  --accent:#a8326f;
  --rule:#d9d9d9;
  --mono-dark:#5e5e5e;
  --mono-light:#d6d6d6;
  --sans:"Questrial","Century Gothic",sans-serif;
  --script:"Great Vibes",cursive;
}
*{margin:0;padding:0;box-sizing:border-box}
html,body{width:1200px;height:406px;overflow:hidden;background:var(--stage)}
body{position:relative;font-family:var(--sans);color:var(--ink)}
.page{position:absolute;top:50px;height:262px;background:var(--paper);overflow:hidden;box-shadow:0 1px 3px rgba(0,0,0,.12)}
.photo{position:absolute}
.mono{background:linear-gradient(160deg,var(--mono-light),var(--mono-dark))}
.t{position:absolute;line-height:1.25}
.tiny{font-size:3.4px;color:var(--soft-ink);line-height:1.35}
.sub{font-size:3.6px;color:var(--ink);text-transform:uppercase;letter-spacing:.2px;margin-top:3px}
.heading{font-size:11px;color:var(--ink);font-weight:400}
.script{font-family:var(--script);color:var(--accent);font-size:10px}
.accent{color:var(--accent)}
.brand{font-size:9px;color:var(--accent)}
.brand-mark{display:inline-block;width:7px;height:7px;border:1px solid var(--accent);vertical-align:-1px;margin-right:3px}
.tagline{font-size:7.5px;color:var(--ink)}
.pkg-col{position:absolute;top:176px;width:54px}
.pkg-name{font-size:7px;color:var(--accent)}
.pkg-price{font-size:3.6px;color:var(--ink);margin:1px 0 3px}
.fee-col{position:absolute;top:176px;width:80px}
.fee-col p{margin-bottom:3px}
.quote-box{position:absolute;left:0;top:8px;width:95px;height:120px;background:rgba(255,255,255,.93);padding:6px}
.quote-head{font-size:8.5px;color:var(--ink);line-height:1.05}
</style>
</head>
<body>

<!-- Spread 1: cover + approach -->
<section class="page cover" style="left:40px;width:185px">
  <div class="photo mono" style="left:0;top:0;width:185px;height:218px" role="img" aria-label="Black and white portrait of a bride in veil holding a white bouquet"></div>
  <div class="t brand" style="left:58px;top:224px"><span class="brand-mark"></span>Clara Pennock</div>
  <div class="t tagline" style="left:34px;top:244px">Your Story. Your Photographer.</div>
</section>

<section class="page approach" style="left:225px;width:185px;box-shadow:none">
  <div class="photo" style="left:75px;top:0;width:110px;height:250px;background:linear-gradient(170deg,#efe6e3,#d9c1c0 45%,#b9aaa0)" role="img" aria-label="Pink and white roses in a glass jar"></div>
  <div class="t heading" style="left:37px;top:8px">Clara's approach...</div>
  <div class="t script" style="left:50px;top:22px">Enjoy your special day!</div>
  <div class="t" style="left:8px;top:62px;width:62px">
    <div class="sub">Style &amp; Approach</div>
    <div class="tiny">Relaxed, natural and elegant images that tell your story. I work quietly in the background, capturing genuine moments as they unfold through the day, with gentle direction for portraits.</div>
    <div class="sub">Formal Photography</div>
    <div class="tiny">Family formals are planned ahead with a short list so nothing is missed and the group shots are finished quickly, leaving more time for you both to enjoy your guests and celebrate together.</div>
    <div class="sub">Image Presentation</div>
    <div class="tiny">Every image is carefully edited by hand and delivered in an online gallery, ready to share, print and keep for years to come.</div>
    <div class="sub">Day of the Wedding</div>
    <div class="tiny">I arrive early, stay calm and keep the day flowing so you can simply relax and be present.</div>
  </div>
</section>

<!-- Spread 2: packages + à la carte -->
<section class="page packages" style="left:420px;width:185px">
  <div class="photo mono" style="left:2px;top:5px;width:66px;height:150px;background:linear-gradient(170deg,#b9b2a6,#5b5a4f)" role="img" aria-label="Bride and groom standing among willow trees"></div>
  <div class="photo" style="left:70px;top:5px;width:115px;height:80px;background:linear-gradient(170deg,#f1ebe7,#c9bab0)" role="img" aria-label="Smiling bride portrait in veil"></div>
  <div class="photo" style="left:70px;top:87px;width:55px;height:68px;background:linear-gradient(170deg,#d8d4cf,#6c6a64)" role="img" aria-label="Couple portrait outdoors"></div>
  <div class="photo" style="left:127px;top:87px;width:58px;height:68px;background:linear-gradient(170deg,#a9a58b,#3f4532)" role="img" aria-label="Bridal party in the garden"></div>
  <div class="t heading" style="left:8px;top:160px">Wedding Packages</div>
  <div class="pkg-col" style="left:8px">
    <div class="pkg-name">Signature</div>
    <div class="pkg-price">Price: $2,420 (value)</div>
    <div class="tiny">• Up to 6 hrs of coverage<br>• Second shooter on the day<br>• Online gallery of images<br>• Edited high resolution files<br>• Print release included<br>• Ten fine art prints<br>• Engagement session</div>
  </div>
  <div class="pkg-col" style="left:66px">
    <div class="pkg-name">Platinum</div>
    <div class="pkg-price">Price: $2,900 (value)</div>
    <div class="tiny">• Up to 8 hrs of coverage<br>• Second shooter on the day<br>• Online gallery of images<br>• Edited high resolution files<br>• Print release included<br>• Premium photo album<br>• Engagement session</div>
  </div>
  <div class="pkg-col" style="left:124px">
    <div class="pkg-name">Gold</div>
    <div class="pkg-price">Price: $3,400 (value)</div>
    <div class="tiny">• Up to 10 hrs of coverage<br>• Second shooter on the day<br>• Online gallery of images<br>• Edited high resolution files<br>• Two premium albums<br>• Parent albums included<br>• Thank you cards</div>
  </div>
</section>

<section class="page fees" style="left:605px;width:185px;box-shadow:none">
  <div class="photo" style="left:3px;top:5px;width:182px;height:140px;background:linear-gradient(170deg,#d7d7d7,#4f4f4f)" role="img" aria-label="Black and white portrait of the couple embracing"></div>
  <div class="t heading" style="left:8px;top:158px">À la Carte Fees to Consider</div>
  <div class="fee-col tiny" style="left:8px">
    <p><span class="accent">Engagement Session</span><br>$250 for a relaxed session</p>
    <p><span class="accent">Digital Negatives</span><br>$490</p>
    <p><span class="accent">Extended Coverage</span><br>$145 per hour</p>
    <p><span class="accent">Online Slideshow</span><br>$160</p>
    <p><span class="accent">Slideshow</span><br>$295</p>
    <p><span class="accent">Second Photographer</span><br>$375</p>
  </div>
  <div class="fee-col tiny" style="left:95px">
    <p><span class="accent">Photo Enlargements</span><br>Canvas or framed prints from $65</p>
    <p><span class="accent">Professional Edited Album</span><br>$770</p>
    <p><span class="accent">Album Upgrades</span><br>From Signature to Platinum $180</p>
    <p><span class="accent">Custom Thank You Cards</span><br>$180 for fifty printed cards</p>
  </div>
</section>

<!-- Spread 3: testimonials + closing -->
<section class="page testimonials" style="left:810px;width:185px">
  <div class="photo" style="left:0;top:0;width:185px;height:262px;background:linear-gradient(160deg,#c8b98c,#8a7a55 50%,#5d5343)" role="img" aria-label="Bride and groom embracing beside a willow tree"></div>
  <div class="quote-box">
    <div class="quote-head">What client's<br>are saying...</div>
    <div class="tiny" style="margin-top:6px">"Thank you so much for our photos. You captured the day perfectly and we could not be happier with them."</div>
    <div class="t script" style="position:static;text-align:right;font-size:8px">Tess</div>
    <div class="tiny">"Thanks so much for photographing our special day. You were amazing and made everyone feel so comfortable and relaxed."</div>
    <div class="t script" style="position:static;text-align:right;font-size:8px">Maya</div>
  </div>
</section>

<section class="page closing" style="left:995px;width:155px;box-shadow:none">
  <div class="photo" style="left:0;top:5px;width:155px;height:140px;background:linear-gradient(170deg,#cfd3c4,#7d8479 50%,#3d3f55)" role="img" aria-label="Bride with bridesmaids in navy dresses on a lawn"></div>
  <div class="t" style="left:8px;top:152px;font-size:7.5px;width:140px;line-height:1.15">How do you want to<br>remember your special day?</div>
  <div class="t tiny" style="left:8px;top:172px;width:80px">Thank you for considering me to capture your wedding day. I would love to hear your plans and chat about how we can tell your story together. Get in touch to book a relaxed meeting.</div>
  <div class="t" style="left:8px;top:218px;font-size:6px;color:var(--accent)"><span class="brand-mark" style="width:5px;height:5px"></span>Clara Pennock</div>
  <div class="t tiny" style="left:8px;top:228px">12 Harbour Street, Brunswick VIC 3056<br>www.clarapennock.com<br>hello@clarapennock.com<br>0400 000 123</div>
</section>

</body>
</html>
```